Sale- Bundle signs

We are looking for a design to use for Permanent SALE/Bundle deal signs. We are a natural bath products company who uses all natural ingredients to create our handmade line of natural products. We love a clean, fresh look and feel. Simple eye-catching that will be a quick glance and they will know the offer.
We would like to have something simple, eye catching that will promote sales on our different products.
Dead Sea Salt Body Scrubs
large 2 for $40
small 3 for $20
Moisturizing Wash with coconut & olive oil
2 for $20
There are several more needed but we are hoping to decide on one template before making all of the signs.
Visit our website here www.brightwillowco.com
Target Market(s)
Our store serves 70% women and the majority of our customers are 30+ years old.
Industry/Entity Type
It Company
Other font styles liked:
- Century Gothic or similar
Look and feel

```html
<!DOCTYPE html>
<html lang="en">
<head>
<meta charset="utf-8">
<title>Bright Willow – Bundle Deals</title>
<link rel="stylesheet" href="https://fonts.googleapis.com/css2?family=Montserrat:wght@400;600;700&family=Questrial&display=swap">
<style>
  :root {
    --teal: #36b09c;
    --teal-text: #3aae9c;
    --sun: #f2eb7e;
    --ink: #222222;
    --paper: #ffffff;
    --edge: #bfe3dc;
  }
  * { margin: 0; padding: 0; box-sizing: border-box; }
  html, body { width: 857px; height: 1200px; overflow: hidden; background: var(--paper); }
  .sign {
    position: relative;
    width: 857px;
    height: 1200px;
    overflow: hidden;
    background: var(--paper);
    border: 1px solid var(--edge);
    font-family: "Montserrat", "Century Gothic", sans-serif;
  }
  .backdrop { position: absolute; inset: 0; width: 100%; height: 100%; }
  .line {
    position: absolute;
    left: 0;
    width: 100%;
    text-align: center;
    line-height: 1;
    white-space: nowrap;
  }
  .brand-name {
    top: 48px;
    font-size: 96px;
    font-weight: 400;
    color: var(--ink);
    letter-spacing: -1px;
  }
  .tagline {
    top: 172px;
    font-family: "Questrial", "Century Gothic", sans-serif;
    font-size: 48px;
    color: var(--ink);
    letter-spacing: 1px;
  }
  .product-title {
    font-size: 51px;
    font-weight: 700;
    color: var(--paper);
  }
  .scrubs-title { top: 352px; }
  .wash-title { top: 748px; font-size: 49px; line-height: 1.28; }
  .offer {
    font-size: 78px;
    font-weight: 600;
    color: var(--teal-text);
  }
  .offer-large { top: 482px; }
  .offer-small { top: 562px; }
  .offer-wash { top: 946px; }
  .website {
    top: 1144px;
    font-size: 35px;
    font-weight: 400;
    color: var(--ink);
  }
</style>
</head>
<body>
  <main class="sign">
    <svg class="backdrop" viewBox="0 0 710 994" preserveAspectRatio="none" aria-hidden="true">
      <rect x="0" y="150" width="710" height="790" fill="var(--teal)"/>
      <ellipse cx="355" cy="47" rx="450" ry="203" fill="var(--paper)"/>
      <ellipse cx="355" cy="484" rx="390" ry="133" fill="var(--sun)"/>
      <ellipse cx="355" cy="835" rx="385" ry="117" fill="var(--sun)"/>
      <ellipse cx="355" cy="1010" rx="520" ry="78" fill="var(--paper)"/>
    </svg>

    <header>
      <div class="line brand-name">Bright Willow</div>
      <div class="line tagline">NATURAL BATH PRODUCTS</div>
    </header>

    <section class="deal">
      <h2 class="line product-title scrubs-title">Dead Sea Salt Body Scrubs</h2>
      <p class="line offer offer-large">Large 2 for $40</p>
      <p class="line offer offer-small">Small 3 for $20</p>
    </section>

    <section class="deal">
      <h2 class="line product-title wash-title">Moisturizing Wash with<br>coconut &amp; olive oil</h2>
      <p class="line offer offer-wash">2 for $20</p>
    </section>

    <footer class="line website">www.brightwillowco.com</footer>
  </main>
</body>
</html>
```